Psychology service brochure

Marketing brochure for a new psychological counselling service.
Our old brochure was too boring and conservative. We are selling our services to GP's, psychiatrists, other health providers and of course potential clients. We'd really like a professional, elegant look that conveys us to be compassionate and conscientious providers of psychological services.
I have included a copy of our old brochure and a copy of the changes we'd like to the text.
Updates
I have included a photo of myself and my business partner. Only the faces are needed, so backgrounds would need to be edited out.
Hello, in consultation with my business partner, we would like
the use of our photos in the brochure please (with backgrounds edited out)
no stock photos of random people
use of abstract or nature/floral motifs suggestive of tranquillity
regards,
Miriam
Target Market(s)
General practitioner doctors, potential clients
Industry/Entity Type
Health
Requirements
Must have
- must include BlairMdITC TT- font for the business name
- must include our signature color Pantone 291 (see attached brochure)
- use of the photos of myself and my business partner (with background edited out please)
- keep use of colours to a minimum, 3 colors maximum, one of which must be Pantone 291
- must include changes to the brochure as outlined in the 'Changes to Pamphlet' document.
Nice to have
- an interesting, eye catching layout.
- interesting use of white spaces
- use of subtle abstract or nature/floral related graphics suggestive of tranquillity
Should not have
- should not include our fee
- stock photos of people

```html
<!DOCTYPE html>
<html lang="en">
<head>
<meta charset="utf-8">
<title>Practice Brochure – Inside Spread</title>
<link href="https://fonts.googleapis.com/css2?family=Jost:wght@300;400;500&display=swap" rel="stylesheet">
<style>
  :root {
    --sky: #a4d3e6;
    --sky-deep: #8ec8de;
    --sky-text: #a9d5e7;
    --paper: #ffffff;
    --fold: #e6eef2;
    --frame: #9a9a9a;
  }
  * { box-sizing: border-box; margin: 0; padding: 0; }
  html, body { width: 1200px; height: 845px; overflow: hidden; background: var(--paper); }
  body { font-family: "Jost", "Futura", sans-serif; font-weight: 300; }

  .spread {
    position: relative; width: 1200px; height: 845px;
    background: var(--paper); border: 1px solid var(--frame); overflow: hidden;
  }
  .top-band { position: absolute; left: 0; right: 0; top: 11px; height: 14px; background: var(--sky); }
  .fold { position: absolute; top: 0; bottom: 0; width: 1px; background: var(--fold); }
  .fold--one { left: 399px; } .fold--two { left: 797px; }

  .wave { position: absolute; left: 0; top: 0; width: 1200px; height: 845px; }

  .panel { position: absolute; top: 0; width: 400px; height: 845px; }
  .panel--one { left: 0; } .panel--two { left: 399px; } .panel--three { left: 797px; }

  .portrait {
    position: absolute; top: 64px; width: 112px; height: 112px; border-radius: 50%;
    border: 2px solid var(--sky); padding: 6px; background: var(--paper);
  }
  .portrait__fill {
    width: 100%; height: 100%; border-radius: 50%;
    background: radial-gradient(circle at 50% 45%, #d9b79b 0%, #8e6a4c 60%, #4f5a3a 100%);
  }
  .panel--one .portrait { left: 266px; }
  .panel--two .portrait { left: 265px; }
  .panel--two .portrait__fill { background: radial-gradient(circle at 50% 45%, #ecd2bd 0%, #c9a98a 55%, #7f9a5c 100%); }

  .upper { position: absolute; top: 121px; left: 54px; width: 304px; }
  .panel--two .upper { left: 47px; width: 310px; }
  .panel--three .upper { left: 41px; width: 316px; }

  .profile-name, .section-title {
    font-weight: 400; color: var(--sky-deep); font-size: 15.5px; line-height: 21px;
  }
  .body-copy {
    color: var(--sky-text); font-size: 13px; line-height: 19.8px; margin-top: 6px;
  }
  .body-copy + .body-copy { margin-top: 6px; }
  .panel--three .section-title { margin-bottom: 40px; }

  .lower {
    position: absolute; top: 556px; left: 54px; width: 312px;
    color: var(--paper); font-size: 13px; line-height: 19.8px;
  }
  .panel--two .lower { left: 47px; width: 312px; }
  .panel--three .lower { left: 41px; width: 300px; top: 558px; }

  .fees__title { font-weight: 500; margin-bottom: 4px; }
  .fees__note { font-weight: 500; margin-top: 16px; }

  .flourish {
    position: absolute; border-radius: 50%;
    background: radial-gradient(circle, rgba(255,255,255,0.35) 0%, rgba(255,255,255,0) 70%);
  }
  .flourish--left { left: 0; top: 670px; width: 150px; height: 175px; }
  .flourish--mid { left: 320px; top: 750px; width: 100px; height: 95px; }
  .flourish--right { left: 1120px; top: 720px; width: 90px; height: 125px; }
</style>
</head>
<body>
<div class="spread">
  <div class="top-band"></div>
  <div class="fold fold--one"></div>
  <div class="fold fold--two"></div>

  <svg class="wave" viewBox="0 0 1200 845" aria-hidden="true">
    <path d="M0 505 C 150 470, 300 455, 420 458 C 600 462, 720 500, 860 512 C 980 522, 1100 518, 1200 512 L1200 845 L0 845 Z" fill="#a4d3e6"/>
    <path d="M0 522 C 150 484, 300 470, 420 472 C 600 476, 720 514, 860 526 C 980 536, 1100 532, 1200 528 L1200 845 L0 845 Z" fill="#ffffff"/>
    <path d="M0 530 C 150 492, 300 478, 420 480 C 600 484, 720 522, 860 534 C 980 544, 1100 540, 1200 536 L1200 845 L0 845 Z" fill="#a4d3e6"/>
  </svg>

  <div class="flourish flourish--left" role="img" aria-label="Soft floral swirl ornament"></div>
  <div class="flourish flourish--mid" role="img" aria-label="Soft floral swirl ornament"></div>
  <div class="flourish flourish--right" role="img" aria-label="Soft floral swirl ornament"></div>

  <section class="panel panel--one">
    <div class="portrait"><div class="portrait__fill" role="img" aria-label="Portrait photo of Miriam Hallett"></div></div>
    <div class="upper">
      <h2 class="profile-name">Miriam Hallett<br>Clinical Psychologist<br>M.Psych (Clin.) MAPS</h2>
      <p class="body-copy">Miriam is a Clinical Psychologist with fifteen years of experience providing a range of psychological services to challenging clients within the public mental health sector including forensic, addiction and dual diagnosis services. She has been employed as a Senior Psychologist in this capacity for the last seven years.</p>
      <p class="body-copy">Miriam is a trained and experienced Cognitive Behavioural Therapist and is skilled in treating individuals and groups with a range of mood disorders including anxiety, depression and panic disorder, as well as in helping clients to overcome life issues such as grief and loss, stress management and anger management.</p>
    </div>
    <p class="lower">Miriam trains other mental health clinicians and university students in treatment modalities including Motivational Interviewing and Brief Interventions. She has an interest in brain-based research into neuroplasticity and it’s application to cognitive therapy and change.</p>
  </section>

  <section class="panel panel--two">
    <div class="portrait"><div class="portrait__fill" role="img" aria-label="Portrait photo of Joanna Pryce"></div></div>
    <div class="upper">
      <h2 class="profile-name">Joanna Pryce<br>Psychologist<br>M.Psych (Clin.) MAPS</h2>
      <p class="body-copy">Joanna is a Psychologist, and with fifteen years experience working in the public health sector, seven as a Senior Psychologist, she is a highly skilled clinician in the areas of mental health, addiction and dual diagnosis.</p>
      <p class="body-copy">She has more recently specialised in working with adolescents but has significant experience treating adults, both individually and in a variety of group programmes. She has also facilitated numerous training events and mentored clinicians in addressing dual diagnosis issues with their clients.</p>
    </div>
    <p class="lower">Joanna primarily utilises a cognitive behavioural framework, motivational interviewing, and has a special interest in working with adolescents who are experiencing developmental difficulties, antenatal and post-natal depression/stress, and parenting issues. Additionally Joanna is skilful working in the areas of grief &amp; loss, life transition and adjustment issues, relationship and interpersonal challenges, and personal development.</p>
  </section>

  <section class="panel panel--three">
    <div class="upper">
      <h2 class="section-title">Our Fee Structure</h2>
      <p class="body-copy">The practice accepts referrals from self-referring individuals, as well as from health professionals such as GPs, Psychiatrists, and Maternal and Child Health Nurses.</p>
      <p class="body-copy">Medicare rebates are available for clients referred for treatment by their GP.</p>
      <p class="body-copy">There are different tiers of rebates for Psychologists under Medicare, and this is dependent on treatment received (individual, group or pregnancy support counselling), and whether you are treated by a Psychologist or a Clinical Psychologist.</p>
      <p class="body-copy">Please contact us directly to further discuss fees for treatment.</p>
    </div>
    <div class="lower fees">
      <p class="fees__title">Psychologist Fees:</p>
      <p>Fees are paid in full at the end of each session, and a receipt is provided which will allow you to obtain your refund at any Medicare office.</p>
      <p class="fees__note">The practice does not bulk bill at this time, but we anticipate the addition of this facility in the future.</p>
    </div>
  </section>
</div>
</body>
</html>
```